The Lament of the Hollow Sonata - eBook Cover

Greetings, artists,

***Update*** A design has come in that I really like - I will probably pick this design. If artists would like to submit potential designs before the end of the contest (Friday), I am VERY happy to consider them, but, respecting your time, I thought you should know where the situation stands. :)

The name of the eBook story: The Lament of the Hollow Sonata
Name of the writer: Theodore Brisk

Blurb: "New York City, 1910. The great composer Gustav Mahler is fleeing a curse that killed Beethoven, Schubert, Dvorak, and a score of other great composers before him, The Lament of the Hollow Sonata. Each of these men died upon completing their ninths, and Mahler is convinced that he will perish now that he’s completed his. A mysterious gentleman in black is stalking the composer. His marriage to his beautiful wife Alma, twenty years his junior, appears to be disintegrating before his very eyes. Is the composer’s desperate terror a delusion, or are the Heavens aligned against the writing of another symphony?"

The feeling that I am seeking from the cover is of something ominous, something unnerving, disturbing, something off. I would like it to evoke some mystery or dread.

I leave the cover up to the imagination of the artist but here are two images that I think hold strong potential:

A) The image of a blue eye in darkness. I have attached an excellent creative commons image that I think may work for this purpose. I wonder if it could be edited to add a burst of amber around the pupil to reflect this description,""...There was something strange about his eyes. They were blue, with a burst of amber around the irises. His gaze pierced Gustav the way a needle pierces cotton."

or

B) the image of the Angel Of Waters statue on top of the Bethesda Fountain (zoomed in on the statue), Central Park. I have attached a creative commons image that may be helpful or other images could be better.

or

C) A combination of the two

The story takes place in 1910, and the cover should have a historic feel. I would like it to be striking and eye-catching, inducing the reader to want to check it out.

Really excited to see your work! If you have any questions, hit me up at theobrisk@quillpost.example, or call at 555-284-1936.

Thank you in advance for your hard work,

Theo

PS Please see Must Haves for technical requirements

PPS I have uploaded the story as a document, if you want to check it out.
Updates

Dear Designers,

I have received a number of incredible designs from you. A design has come in that I really like - I will probably pick this design. If artists would like to submit potential designs before the end of the contest (Friday), I am VERY happy to consider them, but, respecting your time, I thought you should know where the situation stands. :) 

Thank you for your incredible work, 

Looking forward to working with many of you in the future, 

Theo

Dear Designers,

Just wanted to write this brief note to thank you for all of your hard work on these designs. This is my first time using ArtHarbor, and it was an amazing, inspiring experience. 

A special thank you goes out to Lanternfold Studio, plumwhistle, TorvenK, Kelpo4, RUX8 and Quarrymaker of submitting multiple designs and taking the time to play with revisions. Your professionalism is remarkable, and I will be honored to invite you to my projects in the future. 

A separate special thank you to Bettina Crowle whose beautiful and very unique design was a pleasure to behold. 

And big shout outs and thank yous to finch413kt, loom5craft, pmolt, Glimmerhook, Caddlewick Forge, PLN and Ravin Telwatte. Fascinating, inspiring designs. 

So, in summary, thanks for taking part in this project and I hope to see all of you guys in the next contest, coming about a month down the line. 

Cheers, 

Theo

Target Market(s)

Adult readers interested in historical fiction.

Industry/Entity Type

Artists

Requirements
Must have
• Please see the bookvale guide for ebook images for full specs. These specs will be absolutely required for the image. :)

https://pub.bookvale.example/self-publishing/help?topicId=Q7X3LM9PZE2RKD
Should not have
• The image should not feel too modern.

```html
<!DOCTYPE html>
<html lang="en">
<head>
<meta charset="utf-8">
<title>The Lament of the Hollow Sonata — eBook Cover</title>
<link rel="stylesheet" href="https://fonts.googleapis.com/css2?family=Cinzel:wght@400;500&family=Pinyon+Script&display=swap">
<style>
  :root {
    --night: #0d1214;
    --slate: #2a3235;
    --fog: #3b4547;
    --silver: #e2e5e8;
    --iris: #7d93a4;
    --iris-deep: #3e5262;
    --amber: #ff8a1c;
    --ember: #b8480a;
  }
  html, body {
    margin: 0;
    padding: 0;
    width: 751px;
    height: 1200px;
    overflow: hidden;
    background: var(--night);
  }
  .cover {
    position: relative;
    width: 751px;
    height: 1200px;
    overflow: hidden;
    font-family: "Cinzel", "Times New Roman", serif;
    color: var(--silver);
  }
  .backdrop {
    position: absolute;
    inset: 0;
    background:
      radial-gradient(ellipse 55% 28% at 45% 14%, var(--fog) 0%, transparent 70%),
      radial-gradient(ellipse 70% 45% at 50% 48%, var(--slate) 0%, transparent 75%),
      linear-gradient(180deg, #1b2326 0%, var(--night) 55%, #151d20 100%);
  }
  .eye-photo {
    position: absolute;
    left: 130px;
    top: 420px;
    width: 500px;
    height: 220px;
    border-radius: 50%;
    background:
      radial-gradient(circle at 50% 50%, var(--iris-deep) 0, var(--iris) 60px, rgba(255, 138, 28, 0.8) 96px, rgba(184, 72, 10, 0.35) 112px, transparent 140px),
      radial-gradient(ellipse at 50% 50%, rgba(120, 130, 135, 0.5) 0, transparent 70%);
  }
  .title {
    margin: 0;
    font-weight: 400;
    text-shadow: 0 3px 6px rgba(0, 0, 0, 0.85);
  }
  .title-line {
    position: absolute;
    left: 0;
    right: 0;
    display: flex;
    justify-content: center;
    align-items: baseline;
    line-height: 1;
    white-space: nowrap;
  }
  .line-the    { top: 232px; font-size: 76px; letter-spacing: 2px; }
  .line-lament { top: 300px; font-size: 88px; letter-spacing: 1px; }
  .line-of     { top: 392px; font-size: 66px; letter-spacing: 2px; }
  .line-hollow { top: 640px; font-size: 100px; letter-spacing: 1px; }
  .line-sonata { top: 800px; font-size: 100px; letter-spacing: 1px; }
  .initial {
    font-family: "Pinyon Script", "Brush Script MT", cursive;
    font-size: 190px;
    line-height: 1;
    margin-right: 6px;
  }
  .author {
    position: absolute;
    left: 0;
    right: 0;
    top: 1064px;
    margin: 0;
    text-align: center;
    font-size: 56px;
    font-weight: 400;
    line-height: 1;
    letter-spacing: 2px;
    text-shadow: 0 3px 6px rgba(0, 0, 0, 0.85);
  }
</style>
</head>
<body>
  <main class="cover">
    <div class="backdrop" role="img" aria-label="Dark smoky collage of an angel statue, faded sheet music and a treble clef"></div>
    <div class="eye-photo" role="img" aria-label="Photograph of a blue eye in darkness with a burst of amber around the iris"></div>

    <h1 class="title">
      <span class="title-line line-the">THE</span>
      <span class="title-line line-lament">LAMENT</span>
      <span class="title-line line-of">OF THE</span>
      <span class="title-line line-hollow"><span class="initial">H</span>OLLOW</span>
      <span class="title-line line-sonata"><span class="initial">S</span>ONATA</span>
    </h1>

    <p class="author">THEODORE BRISK</p>
  </main>
</body>
</html>
```